Brightpath EAP 2 x Flyer with Poster

Brightpath is an award-winning organisation providing dynamic and creative ways for children, young people, adults and families to make positive change and achieve fulfilling lives.
We are launching into a new area of business and starting to offer organisations Employee Assistance Program (EAP). To launch this service we need 2 flyers and a poster:
- 1 x flyer for employers
- 1 x flyer for employees
- 1 x poster (A3) for employees to be displayed around the office.
For the flyers we are after an a4 colour double sided flyer in either a A4 tri-fold to DL format or A4 bi-fold to A5 format. We are looking for a design that is simple and dynamic whilst keeping in line with our branding.
The winning designs will need to be hi-res and ready for print and also a lower res version suitable to email.
I have attached a number of files to provide further background, including:
• I have attached 3 x word doc of copy for each (2 x flyer / 1 x poster)
• Brand Guidelines
• Logo
• Our clinic flyer recently produced by a ArtHive designer for our clinic area of the business. These flyers do not have to be exactly the same as this one but should appear to be from the same organisation although a different service.
Generally we like our designs to be clear and simple.
Please don't hesitate to reach out with any Q's.

```html
<!DOCTYPE html>
<html lang="en">
<head>
<meta charset="utf-8">
<title>Brightpath EAP Poster</title>
<link href="https://fonts.googleapis.com/css2?family=Hind:wght@400;500;600;700&display=swap" rel="stylesheet">
<style>
  :root{
    --bg:#e4e4e2;
    --paper:#f7f7f5;
    --slate:#7f979e;
    --slate-dark:#6b8790;
    --sage:#7b907a;
    --tan:#c9a594;
    --tan-light:#d9b9a9;
    --ink:#3f4143;
    --ink-soft:#4d5053;
    --white:#ffffff;
  }
  *{box-sizing:border-box;margin:0;padding:0}
  html,body{width:1200px;height:801px;overflow:hidden;background:var(--bg);font-family:"Hind",sans-serif;color:var(--ink)}
  .poster{position:absolute;left:322px;top:10px;width:556px;height:781px;background:var(--paper);box-shadow:0 2px 10px rgba(0,0,0,.12);overflow:hidden}
  .header{position:absolute;left:0;top:0;width:556px;height:94px}
  .brand{position:absolute;left:26px;top:26px;display:flex;align-items:center;gap:10px}
  .brand-dot{width:40px;height:40px;border-radius:50%;background:var(--sage)}
  .brand-name{font-size:38px;font-weight:600;color:var(--ink);line-height:1;letter-spacing:-.3px}
  .contact-panel{position:absolute;right:0;top:0}
  .contact-list{position:absolute;left:348px;top:22px;list-style:none}
  .contact-list li{display:flex;align-items:center;gap:8px;color:var(--white);font-size:17px;font-weight:500;height:25px}
  .contact-list svg{flex:none}
  .contact-list .phone{font-weight:600;font-size:18px}
  .photo{position:absolute;left:0;top:94px;width:556px;height:248px;background:radial-gradient(ellipse at 50% 55%,#9a9a9a 0%,#6d6d6d 45%,#3b3b3b 100%)}
  .title-band{position:absolute;left:0;top:342px;width:556px;height:71px;background:var(--sage);text-align:center;padding-top:9px}
  .title-band h1{font-size:21px;font-weight:700;color:var(--tan-light);letter-spacing:.3px;line-height:1.15}
  .title-band h2{font-size:22px;font-weight:600;color:var(--white);line-height:1.3}
  .content{position:absolute;left:23px;top:418px;width:512px;display:flex;justify-content:space-between}
  .col{width:246px}
  .col h3{font-size:13px;font-weight:600;color:var(--slate-dark);line-height:1.2;margin-bottom:2px}
  .col p{font-size:7.9px;line-height:10.9px;color:var(--ink-soft);text-align:justify}
  .col section{margin-bottom:16px}
  .col .lead{font-weight:600;color:var(--ink)}
  .services{display:flex;gap:14px;margin-top:4px}
  .services ul{list-style:none;width:112px}
  .services li{position:relative;padding-left:11px;font-size:7.9px;line-height:10.9px;color:var(--ink-soft);margin-bottom:5px}
  .services li::before{content:"";position:absolute;left:1px;top:3px;width:4px;height:4px;border-radius:50%;background:var(--slate)}
  .footer{position:absolute;left:0;top:706px;width:556px;height:75px}
  .appointment{position:absolute;left:24px;top:12px;width:240px;color:var(--white)}
  .appointment h4{font-size:12.5px;font-weight:600;line-height:1.2}
  .appointment p{font-size:7.7px;line-height:10.8px}
  .location{position:absolute;left:268px;top:24px;color:var(--white);font-size:8.5px;line-height:12px}
  .location strong{font-size:10.5px;font-weight:700;display:block;letter-spacing:.3px}
  .location .row{display:flex;align-items:center;gap:4px}
  .location .addr{padding-left:12px;display:flex;gap:8px;align-items:center}
</style>
</head>
<body>
<main class="poster">
  <header class="header">
    <div class="brand">
      <span class="brand-dot"></span>
      <span class="brand-name">Brightpath</span>
    </div>
    <svg class="contact-panel" width="260" height="94" viewBox="0 0 260 94">
      <polygon points="38,0 260,0 260,94 0,94" fill="var(--tan)"/>
      <polygon points="46,0 260,0 260,94 10,94" fill="var(--slate)"/>
    </svg>
    <ul class="contact-list">
      <li class="phone">
        <svg width="17" height="17" viewBox="0 0 17 17"><circle cx="8.5" cy="8.5" r="8.5" fill="var(--tan-light)"/><path d="M5.6 4.3l1.6-.3.9 2.2-1.1.8a6 6 0 0 0 2.9 2.9l.8-1.1 2.2.9-.3 1.6c-4 .6-7.6-3-7-7z" fill="var(--white)"/></svg>
        (03) 9000 4521
      </li>
      <li>
        <svg width="17" height="17" viewBox="0 0 17 17"><circle cx="8.5" cy="8.5" r="8.5" fill="var(--tan-light)"/><rect x="4.3" y="5.6" width="8.4" height="5.8" fill="none" stroke="var(--white)" stroke-width="1"/><path d="M4.3 5.6l4.2 3.2 4.2-3.2" fill="none" stroke="var(--white)" stroke-width="1"/></svg>
        clinic@brightpath.au
      </li>
    </ul>
  </header>

  <div class="photo" role="img" aria-label="Black and white photo of many hands reaching into a circle, fingertips touching to form a star"></div>

  <div class="title-band">
    <h1>EMPLOYEE ASSISTANCE PROGRAM (EAP)</h1>
    <h2>Counselling for Work Related or Personal Issues</h2>
  </div>

  <div class="content">
    <div class="col">
      <section>
        <h3>Employee Assistance Program</h3>
        <p>Employee Assistance Program (EAP) is a confidential employer-funded support service available to employees and immediate family members experiencing personal or work-related concerns. Immediate family include your spouse, partner, children or others living in your household.</p>
      </section>
      <section>
        <h3>Counselling Services</h3>
        <p class="lead">EAP is provided for a variety of personal, emotional and work-related matters including:</p>
        <div class="services">
          <ul>
            <li>Anxiety</li>
            <li>Depression and emotional wellbeing</li>
            <li>Workplace conflict or disharmony</li>
            <li>Coping with organisational change</li>
            <li>Stress and burnout</li>
            <li>Bullying</li>
            <li>Sexual harassment</li>
          </ul>
          <ul>
            <li>Self-esteem</li>
            <li>Reactions to traumatic or distressing events</li>
            <li>Critical incidents</li>
            <li>Grief and bereavement</li>
            <li>Substance misuse</li>
            <li>Domestic violence</li>
            <li>Interpersonal relationships</li>
            <li>Schooling and study difficulties.</li>
          </ul>
        </div>
      </section>
    </div>
    <div class="col">
      <section>
        <h3>Who Pays for the Service?</h3>
        <p>Your employer will pay for an agreed number of sessions. You are not required to pay for using the Brightpath EAP service. The number of available sessions depends on the agreement we have with your employer.</p>
      </section>
      <section>
        <h3>Is it Confidential?</h3>
        <p>All employee personal information collated by Brightpath during the provision of counselling services will remain confidential and secure except when subpoenaed by a court or failure to disclose the information would place the employee and/or another person at risk. Confidentiality and limitations of confidentiality are explained to employees at the beginning of the counselling process.</p>
      </section>
      <section>
        <h3>About Brightpath</h3>
        <p>Brightpath provides a confidential and effective counselling process that is solution-focused and practical. The service is aimed at enhancing wellbeing and mental health, and can be accessed via face-to-face consultations, and by Telehealth or phone. Accessing assistance is an act of independence and strength which can empower you to make positive changes in your life.</p>
      </section>
    </div>
  </div>

  <footer class="footer">
    <svg width="556" height="75" viewBox="0 0 556 75" style="position:absolute;left:0;top:0">
      <polygon points="250,14 556,14 556,64 240,64" fill="var(--tan)"/>
      <polygon points="0,0 264,0 244,70 0,70" fill="var(--slate)"/>
      <polygon points="264,0 268,12 248,70 244,70" fill="var(--slate-dark)"/>
    </svg>
    <div class="appointment">
      <h4>How do I make an EAP Appointment?</h4>
      <p>You can make a confidential appointment directly with Brightpath through our direct line on 03 9000 4521 or via clinic@brightpath.au</p>
    </div>
    <div class="location">
      <strong>BRIGHTPATH</strong>
      <div class="row">
        <svg width="8" height="8" viewBox="0 0 8 8"><circle cx="4" cy="4" r="4" fill="var(--tan-light)"/><circle cx="4" cy="3.4" r="1.4" fill="var(--white)"/></svg>
        Harbourline Building
      </div>
      <div class="addr">
        <span>42 Wattle Grove, Northvale VIC 3100</span>
        <span class="row"><svg width="8" height="8" viewBox="0 0 8 8"><circle cx="4" cy="4" r="3.5" fill="none" stroke="var(--white)" stroke-width=".8"/><path d="M.5 4h7M4 .5v7" stroke="var(--white)" stroke-width=".6"/></svg>www.brightpath.au</span>
      </div>
    </div>
  </footer>
</main>
</body>
</html>
```